Wohnhof am Weiher - Zeitungsinserat für den Verkauf von Eigentumswohnungen

Wir brauchen ein Zeitungsinserat in zwei Formaten. Einmal 296 Breite x 440 Höhe mm und einmal 296 Breite x 220 mm Höhe.
Als Basis dient der sehr grobe Entwurf im Powerpoint (Entwurf.pptx).
Auf dem Entwurf fehlen noch die Kontaktangeben:
Brunnhofer Liegenschaften AG
Seematteweg 14
4387 Tannried
079 462 37 58
rbrunnhofer@tessin-ostwald.ch

Zudem muss noch der Link auf die Webseite aufgeführt werden.
www.wohnhof-am-weiher.ch

Zudem fehlt noch der Text:
Fordern Sie noch heute die Verkaufsunterlagen gedruckt oder per Email an. Schreiben Sie uns einfach eine Chatpost mit Ihrer Adresse.

Ich habe noch Files von den Innenvisualisierungen, den Aussenvisualisierungen sowie unser Logo hinzugefügt. Zudem habe ich Ihnen die Verkaufsbrochure angefügt. Sie können die Daten vom Entwurf gerne ergänzen wenn Ihnen etwas gefällt. Schön wäre es, wenn Sie den Stil ähnlich machen würden wie die Brochure.

Target Market(s)

Famillien, Paare und Rentner

Font styles to use
Serif

Colors

Designer to choose colors to be used in the design.

Requirements
Must have
• Tolles Design das sofort anspricht!

```html
<!DOCTYPE html>
<html lang="de">
<head>
<meta charset="utf-8">
<title>Wohnhof am Weiher – Inserat</title>
<link href="https://fonts.googleapis.com/css2?family=Source+Serif+4:opsz,wght@8..60,400;8..60,600;8..60,700&display=swap" rel="stylesheet">
<style>
:root{
  --blue:#0a8ad2;
  --blue-band:#1b8fd4;
  --ink:#2b2b2b;
  --cell:rgba(222,224,226,0.9);
  --panel:rgba(255,255,255,0.55);
  --head:rgba(40,150,215,0.8);
}
*{margin:0;padding:0;box-sizing:border-box}
html,body{width:1200px;height:807px;overflow:hidden;background:#fff}
body{font-family:"Source Serif 4",Georgia,serif;color:var(--ink);position:relative}
.hero{position:absolute;left:0;top:0;width:1200px;height:502px;
  background:linear-gradient(180deg,#a9cbe8 0%,#d7e7f3 30%,#e9eef0 48%,#b9c4c8 58%,#7fa36b 72%,#5b8a44 100%)}
.title{position:absolute;top:32px;left:0;width:1200px;text-align:center;font-weight:700;font-size:54px;line-height:64px;color:var(--blue);letter-spacing:-0.5px}
.subtitle{position:absolute;top:103px;left:0;width:1200px;text-align:center;font-weight:600;font-size:16.5px;color:#333}
.pin{position:absolute;width:14px;height:14px;border-radius:50%;background:#39a7e6;border:2px solid #bfe3f8}
.house{position:absolute;top:260px;height:242px;background:var(--panel)}
.house-name{height:26px;background:var(--head);color:#fff;font-weight:700;font-size:19px;text-align:center;line-height:27px}
table{position:absolute;border-collapse:collapse;table-layout:fixed;font-size:7.5px;line-height:10px}
td{background:var(--cell);border:1px solid #fff;vertical-align:top;padding:4px 3px 3px 5px;overflow:hidden}
.thumb{position:absolute;top:503px;height:53px}
.interior{background:linear-gradient(135deg,#e9e9e7,#c9c6c0 60%,#8e8a84)}
.plan{background:linear-gradient(135deg,#e3e4e2,#bfc2bd 55%,#7b7f78)}
.feature{position:absolute}
.feature h3{font-size:12px;font-weight:700;line-height:16px;color:#333}
.feature p{font-size:10.3px;line-height:14.2px;color:#333}
.tick{position:absolute;width:22px;height:22px}
.cta{position:absolute;top:735px;left:0;width:1200px;text-align:center;font-weight:700;font-size:15.3px;color:var(--blue)}
.contact{position:absolute;left:0;top:767px;width:1200px;height:40px;background:var(--blue-band);color:#fff;font-weight:600;font-size:12.6px;display:flex;align-items:center;justify-content:center;gap:16px;white-space:nowrap}
.contact span{display:flex;align-items:center}
.contact svg{margin-right:6px}
.contact .lead{font-weight:700;font-size:14px}
</style>
</head>
<body>
<div class="hero" role="img" aria-label="Aussenvisualisierung der drei Mehrfamilienhäuser mit Garten, Bäumen und Himmel"></div>
<div class="title">Wohnhof am Weiher</div>
<div class="subtitle">Hochwertige und moderne Eigentumswohnungen</div>

<svg width="1200" height="502" style="position:absolute;left:0;top:0">
  <line x1="239" y1="185" x2="239" y2="262" stroke="#fff" stroke-width="0.8"/>
  <line x1="665" y1="215" x2="600" y2="262" stroke="#fff" stroke-width="0.8"/>
  <line x1="937" y1="215" x2="990" y2="262" stroke="#fff" stroke-width="0.8"/>
</svg>
<div class="pin" style="left:232px;top:178px"></div>
<div class="pin" style="left:658px;top:208px"></div>
<div class="pin" style="left:930px;top:208px"></div>

<section class="house" style="left:84px;width:296px"><div class="house-name">Haus A</div></section>
<table style="left:100px;top:302px;width:265px">
  <colgroup><col style="width:44px"><col style="width:50px"><col style="width:34px"><col style="width:68px"><col style="width:69px"></colgroup>
  <tr style="height:38px"><td>Attika</td><td>4.5<br>Zimmer</td><td>108m²</td><td>105m²<br>Sonnenterrasse</td><td>945’000 CHF</td></tr>
  <tr style="height:28px"><td>Oberges<br>choss</td><td>3.5<br>Zimmer</td><td>81m²</td><td>16m² Balkon</td><td>754’800 CHF</td></tr>
  <tr style="height:27px"><td>Oberges<br>choss</td><td>4.5<br>Zimmer</td><td>102m</td><td>33m² Balkon</td><td>640’000 CHF</td></tr>
  <tr style="height:48px"><td>Erdgesc<br>hoss</td><td>3.5<br>Zimmer</td><td>81m²</td><td>16m²<br>gedeckter<br>Sitzplatz &amp;<br>eigener Garten</td><td>657’000 CHF</td></tr>
  <tr style="height:49px"><td>Erdgesc<br>hoss</td><td>4.5<br>Zimmer</td><td>102m</td><td>33m²<br>gedeckter<br>Sitzplatz &amp;<br>eigener Garten</td><td>765’000 CHF</td></tr>
</table>

<section class="house" style="left:452px;width:304px"><div class="house-name">Haus B</div></section>
<table style="left:465px;top:301px;width:278px;font-size:8px">
  <colgroup><col style="width:67px"><col style="width:45px"><col style="width:39px"><col style="width:73px"><col style="width:54px"></colgroup>
  <tr style="height:36px"><td>Attika</td><td>4.5<br>Zimmer</td><td>109m²</td><td>107m²<br>Sonnenterrasse</td><td>965’000<br>CHF</td></tr>
  <tr style="height:29px"><td>Obergeschoss</td><td>2.5<br>Zimmer</td><td>69m²</td><td>14m² Balkon</td><td>550’000<br>CHF</td></tr>
  <tr style="height:29px"><td>Obergeschoss</td><td>4.5<br>Zimmer</td><td>117m²</td><td>42m² Balkon</td><td>877’500<br>CHF</td></tr>
  <tr style="height:40px"><td>Erdgeschoss</td><td>2.5<br>Zimmer</td><td>69m²</td><td>14m² gedeckter<br>Sitzplatz &amp;<br>eigener Garten</td><td>560’000<br>CHF</td></tr>
  <tr style="height:41px"><td>Erdgeschoss</td><td>4.5<br>Zimmer</td><td>117m²</td><td>42m² gedeckter<br>Sitzplatz &amp;<br>eigener Garten</td><td>889’000<br>CHF</td></tr>
</table>

<section class="house" style="left:831px;width:301px"><div class="house-name">Haus C</div></section>
<table style="left:845px;top:301px;width:273px">
  <colgroup><col style="width:64px"><col style="width:45px"><col style="width:42px"><col style="width:70px"><col style="width:52px"></colgroup>
  <tr style="height:35px"><td>Attika</td><td>4.5<br>Zimmer</td><td>129m²</td><td>132m²<br>Sonnenterrasse</td><td>1’125’000<br>CHF</td></tr>
  <tr style="height:27px"><td>Obergeschoss</td><td>5.5<br>Zimmer</td><td>143m²</td><td>43m² Balkon</td><td>1’058’000<br>CHF</td></tr>
  <tr style="height:28px"><td>Obergeschoss</td><td>3.5<br>Zimmer</td><td>96m²</td><td>23m² Balkon</td><td>730’000<br>CHF</td></tr>
  <tr style="height:48px"><td>Erdgeschoss</td><td>5.5<br>Zimmer</td><td>143m²</td><td>43m²<br>gedeckter<br>Sitzplatz &amp;<br>eigener Garten</td><td>1’065’000<br>CHF</td></tr>
  <tr style="height:49px"><td>Erdgeschoss</td><td>3.5<br>Zimmer</td><td>96m²</td><td>23m²<br>gedeckter<br>Sitzplatz &amp;<br>eigener Garten</td><td>740’000<br>CHF</td></tr>
</table>

<div class="thumb interior" style="left:136px;width:90px" role="img" aria-label="Innenvisualisierung Wohnen und Essen Haus A"></div>
<div class="thumb plan" style="left:237px;width:90px" role="img" aria-label="Grundriss einer Wohnung Haus A"></div>
<div class="thumb interior" style="left:508px;width:92px" role="img" aria-label="Innenvisualisierung Wohnbereich Haus B"></div>
<div class="thumb plan" style="left:609px;width:91px" role="img" aria-label="Grundriss einer Wohnung Haus B"></div>
<div class="thumb interior" style="left:894px;width:91px" role="img" aria-label="Innenvisualisierung Küche Haus C"></div>
<div class="thumb plan" style="left:991px;width:78px" role="img" aria-label="Grundriss einer Wohnung Haus C"></div>

<svg style="display:none"><symbol id="tick" viewBox="0 0 22 22"><circle cx="11" cy="11" r="9.8" fill="none" stroke="#1b8fd4" stroke-width="1.4"/><path d="M6.5 11.3l3 3 6-6.3" fill="none" stroke="#1b8fd4" stroke-width="1.5" stroke-linecap="round" stroke-linejoin="round"/></symbol></svg>

<svg class="tick" style="left:82px;top:571px"><use href="#tick"/></svg>
<div class="feature" style="left:119px;top:571px;width:290px"><h3>Bus und Bahn</h3><p>Der Bahnhof von Laufen mit Zugverbindungen nach Basel (20 Minuten) und Delemont ist in wenigen Minuten mit dem Bus zu erreichen.</p></div>
<svg class="tick" style="left:82px;top:644px"><use href="#tick"/></svg>
<div class="feature" style="left:119px;top:644px;width:300px"><h3>Basel – Stadt</h3><p>Der nahegelegene Bahnhof in Laufen verfügt über sehr gute Verbindungen nach Basel (20 Minuten), welche durch den Doppelspurausbau in den kommenden Jahren sogar noch weiter verbessert werden.</p></div>

<svg class="tick" style="left:445px;top:571px"><use href="#tick"/></svg>
<div class="feature" style="left:487px;top:571px;width:355px"><h3>Autobahn</h3><p>Die Wohnsiedlung ist ideal auch für den Individualverkehr erschlossen. Die Entfernung zur Autobahn J18 beträgt 12km und ist über Aesch nnerhalb von 15 Minuten erreichbar.</p></div>
<svg class="tick" style="left:445px;top:644px"><use href="#tick"/></svg>
<div class="feature" style="left:487px;top:644px;width:350px"><h3>Erholung im Grünen</h3><p>Tannried erfüllt mit seinen Wäldern, dem eigenen «Dorfberg» dem «Stürmenkopf», den offenen Feldern, den Wander- und Velorouten und der ländlichen Ruhe alle Voraussetzungen, die ein Naherholungsgebiet begehrt machen.</p></div>

<svg class="tick" style="left:882px;top:571px"><use href="#tick"/></svg>
<div class="feature" style="left:917px;top:571px;width:225px"><h3>Einkaufen und weitere<br>Dienstleistungen</h3><p>Durch die Nähe der Gemeindegrenze zwischen Laufen und Tannried liegen die Dorfzentren mit ihren Einkaufsmöglichkeiten (z.B. Auen Center Laufen sowie der Altstadt in Laufen) und Dienstleistungsangeboten in max. 2 Minuten Fahrtzeit oder in 10-15 Minuten Gehdistanz.</p></div>

<div class="cta">Fordern Sie noch heute die Verkaufsunterlagen gedruckt oder per Email an. Schreiben Sie uns einfach eine Chatpost mit Ihrer Adresse.</div>

<footer class="contact">
  <span class="lead">Kontaktieren Sie uns:</span>
  <span><svg width="13" height="17" viewBox="0 0 16 20"><path d="M8 0C3.6 0 0 3.4 0 7.6 0 13 8 20 8 20s8-7 8-12.4C16 3.4 12.4 0 8 0z" fill="#fff"/><circle cx="8" cy="7.5" r="3" fill="#1b8fd4"/></svg>Brunnhofer Liegenschaften AG, Seematteweg 14, 4387 Tannried</span>
  <span><svg width="16" height="16" viewBox="0 0 20 20"><path d="M4 1l3 4-2 2c1 3 4 6 7 7l2-2 4 3-2 3C9 18 2 11 1 3z" fill="#fff"/><path d="M12 2a6 6 0 0 1 6 6M12 5a3 3 0 0 1 3 3" stroke="#fff" stroke-width="1.5" fill="none"/></svg>079 462 37 58</span>
  <span><svg width="18" height="13" viewBox="0 0 22 16"><rect x="0.5" y="0.5" width="21" height="15" fill="#fff"/><path d="M1 1l10 8 10-8M1 15l7-6M21 15l-7-6" stroke="#1b8fd4" stroke-width="1.4" fill="none"/></svg>rbrunnhofer@tessin-ostwald.ch</span>
  <span><svg width="15" height="15" viewBox="0 0 20 20"><circle cx="10" cy="10" r="8.5" fill="none" stroke="#fff" stroke-width="1.6"/><ellipse cx="10" cy="10" rx="3.8" ry="8.5" fill="none" stroke="#fff" stroke-width="1.3"/><path d="M1.5 10h17" stroke="#fff" stroke-width="1.3"/></svg>www.wohnhof-am-weiher.ch</span>
</footer>
</body>
</html>
```